Proofreading business card design needed

I need a business card for a proofreading business based in Kempsey.
It is our business to scour our clients' written word finding and fixing errors.
We: protect people, businesses and organisations from
embarrassment,
safeguard brands and reputations,
save time and money on costly mistakes.
Updates

Hi Everyone,

I need to make a change to my motto - if you have used it.  The last line of my motto needs to say: save you time and money by eliminating costly errors
Sorry about this change, almost at the last minute, but the way it's currently written just didn't put across what I was trying to say.
Thanks
Mara

Target Market(s)

self-publishers, businesses and organisations, research and educational publishers

Industry/Entity Type

Business

Contact Information for Business Card

The Quill Check Studio, Mara Tillbrook, Ph: 0471 392 548, Email: mara.check@quillmail.example, www.thequillcheckstudio.example.au, Po Box 5219, Fernhollow, NR, 2907.

Logo Text

The Quill Check Studio

Logo styles of interest
Abstract Logo
Character Logo
Wordmark Logo
Requirements
Nice to have
• Modern take on proofreading or business images: glasses, written word, red pen or pencil, ruler, magnifying glass etc.
Is it possible to have the following text on the card:
'We: protect people, businesses and organisations from
embarrassment,
save time and money on costly mistakes.'
However, I'm totally open to new ideas/concepts.
Would be happy to see some double-sided business card concepts.

```html
<!DOCTYPE html>
<html lang="en">
<head>
<meta charset="utf-8">
<title>Mara Tillbrook — The Quill Check Studio</title>
<link rel="stylesheet" href="https://fonts.googleapis.com/css2?family=Yellowtail&family=Lobster&family=Caveat:wght@400&family=Orbitron:wght@400&display=block">
<style>
  :root {
    --card-pink: #ff1670;
    --card-pink-deep: #f0105f;
    --card-pink-soft: #ff3a86;
    --ink-white: #ffffff;
    --frame-purple: #4a1f5c;
  }
  html, body {
    margin: 0;
    padding: 0;
    overflow: hidden;
    background: #ffffff;
  }
  .business-card {
    position: relative;
    width: 1200px;
    height: 693px;
    overflow: hidden;
    background: var(--card-pink);
    color: var(--ink-white);
  }
  .damask-backdrop {
    position: absolute;
    inset: 0;
    background: radial-gradient(ellipse at 60% 40%, var(--card-pink-soft) 0%, var(--card-pink) 55%, var(--card-pink-deep) 100%);
  }
  .glasses-art {
    position: absolute;
    left: 849px;
    top: 79px;
    width: 269px;
    height: 107px;
    border-radius: 20px;
    background: linear-gradient(160deg, var(--frame-purple) 0%, #7a2c6a 100%);
    opacity: 0.55;
  }
  .swirl-ornament {
    position: absolute;
    left: 768px;
    top: 418px;
    width: 432px;
    height: 275px;
    background: radial-gradient(ellipse at 85% 70%, rgba(90,10,42,0.35) 0%, rgba(90,10,42,0) 70%);
  }
  .holder-name {
    position: absolute;
    left: 86px;
    top: 52px;
    margin: 0;
    font-family: "Yellowtail", "Lobster", cursive;
    font-weight: 400;
    font-size: 80px;
    line-height: 1;
    letter-spacing: 1px;
    white-space: nowrap;
  }
  .contact-line {
    position: absolute;
    left: 88px;
    margin: 0;
    font-family: "Caveat", cursive;
    font-weight: 400;
    line-height: 1;
    white-space: nowrap;
  }
  .contact-phone { top: 160px; font-size: 58px; }
  .contact-email { top: 283px; font-size: 50px; }
  .contact-web { top: 373px; font-size: 50px; }
  .contact-address { top: 448px; font-size: 62px; }
  .motto {
    position: absolute;
    left: 0;
    width: 1220px;
    top: 574px;
    margin: 0;
    text-align: center;
    font-family: "Orbitron", sans-serif;
    font-size: 22px;
    line-height: 26px;
    white-space: nowrap;
  }
</style>
</head>
<body>
  <main class="business-card">
    <div class="damask-backdrop" role="img" aria-label="Soft pink damask floral pattern covering the card background"></div>
    <div class="glasses-art" role="img" aria-label="Illustration of dark purple reading glasses"></div>
    <div class="swirl-ornament" role="img" aria-label="Dark curling floral swirl ornament in the bottom right corner"></div>

    <h1 class="holder-name">Mara Tillbrook</h1>
    <p class="contact-line contact-phone">Ph: 0471 392 548</p>
    <p class="contact-line contact-email">mara.check@quillmail.example</p>
    <p class="contact-line contact-web">www.thequillcheckstudio.example.au</p>
    <p class="contact-line contact-address">Po Box 5219, Fernhollow, NR, 2907</p>

    <p class="motto">"We: protect people, businesses and organisations from embarrassment,<br>safeguard brands and reputations, save time and money on costly mistakes."</p>
  </main>
</body>
</html>
```